CAMPO DORMIDO

Campo Dormido is a tribute to the hidden treasures of Chile’s majestic mountain landscapes. Each bottle captures the essence of the Andes, where rugged peaks and fertile valleys create the perfect harmony for winemaking. With a label inspired by the mystique of the mountains, Campo Dormido invites you to uncover the rich flavors and stories hidden within its depths—a wine as bold and timeless as the land it comes from. the current design is old and not attractiv at all we want something new

Please create a mysterious, enigmatic label based on the typography and logo attached to the project. We need at least, at the entry level, five varietal products such as Carménère, Cabernet Sauvignon, Merlot, Chardonnay, and Malbec. Later, we would like to add more premium products, like a Reserva, a Special Reserva, or a Limited Edition. The design should be flexible and easily adaptable to accommodate various products while maintaining the same overall aesthetic.

Project Brief – Large-Scale Brand Label Design
We are developing a new large-scale brand with a structured range of wines. Below are the key design elements and specifications for the labels:

Entry-Level Wines (Bordeaux Bottle Shape)
Varietals: Cabernet Sauvignon, Carménère, Merlot, Cabernet-Merlot, Sauvignon Blanc.
Do not mention the word "varietals" on the label.
Next Level – Special Reserve (Burgundy Bottle Shape)
Varietals: Pinot Noir, Chardonnay, Syrah.
The label must include the mention "Special Reserve."
Premium Level – Limited (Heavy Conical Bottle Shape)
Varietal: Carménère-Malbec.
The label must include the mention "Limited."
Top Level – Secret Blend (Heavy Conical Bottle Shape)
Name on the label: "Secret Blend."
General Label Guidelines
Year: Only mention "2024" (do not include the word “vintage”).
Capsules: Use standard-colored capsules only (no branding).
Design Concept: The style should align with our brand identity. Please refer to www.malvorin-vins.example for inspiration and coherence.

Target Market(s)

younger generation,

Industry/Entity Type

Wines producer

Requirements
Must have
• the original logo with the name it is register We need to indicate the varietals Cabernet Sauvignon, the vintage 2024, the region DO Central Valley
Nice to have
• one white wines version of the label on a burgendy bottle shape and one red wines label on bordeau bottles sahpe

```html
<!DOCTYPE html>
<html lang="en">
<head>
<meta charset="utf-8">
<title>Campo Dormido – Cabernet Sauvignon 2024</title>
<link rel="stylesheet" href="https://fonts.googleapis.com/css2?family=EB+Garamond:wght@400&display=swap">
<style>
  :root {
    --band-green: #162d24;
    --band-charcoal: #2a2927;
    --ink-cream: #ede6d2;
    --sky-cream: #e9e3d1;
    --peak-green: #23392f;
    --peak-dark: #101a15;
    --earth-brown: #7b6546;
    --mark-grey: #9a9a98;
  }
  * { margin: 0; padding: 0; box-sizing: border-box; }
  html, body {
    width: 1050px;
    height: 1200px;
    overflow: hidden;
    background: #ffffff;
  }
  .label {
    position: relative;
    width: 1050px;
    height: 1200px;
    font-family: "EB Garamond", Georgia, serif;
    color: var(--ink-cream);
  }
  .varietal-band {
    height: 140px;
    background: var(--band-green);
    display: flex;
    align-items: center;
    justify-content: center;
  }
  .varietal-name {
    font-weight: 400;
    font-size: 42px;
    letter-spacing: 0.36em;
    margin-right: -0.36em;
    line-height: 1;
  }
  .landscape-art {
    height: 788px;
    background:
      radial-gradient(circle at 18% 3%, var(--peak-green) 0 14%, transparent 14.5%),
      linear-gradient(180deg,
        var(--sky-cream) 0%,
        var(--sky-cream) 22%,
        #c9cbbd 40%,
        var(--peak-green) 58%,
        #8d9487 72%,
        var(--peak-dark) 86%,
        var(--earth-brown) 100%);
  }
  .info-band {
    position: relative;
    height: 272px;
    background: var(--band-charcoal);
  }
  .brand-name {
    position: absolute;
    left: 78px;
    top: 26px;
    font-weight: 400;
    font-size: 84px;
    line-height: 0.98;
    letter-spacing: 0.02em;
    color: var(--ink-cream);
  }
  .brand-name span { display: block; }
  .brand-name span + span { padding-left: 28px; }
  .brand-dot {
    position: absolute;
    left: 400px;
    top: 60px;
    width: 48px;
    height: 48px;
    border-radius: 50%;
    background: var(--mark-grey);
  }
  .wine-details {
    position: absolute;
    right: 84px;
    top: 92px;
    text-align: right;
    font-size: 35px;
    line-height: 1;
  }
  .wine-details p + p { margin-top: 30px; }
</style>
</head>
<body>
  <main class="label">
    <header class="varietal-band">
      <h1 class="varietal-name">CABERNET SAUVIGNON</h1>
    </header>
    <div class="landscape-art" role="img" aria-label="Painted illustration of snow-streaked Andes peaks in deep green and cream under a dark sun with a ringed halo and a misty sky"></div>
    <footer class="info-band">
      <h2 class="brand-name"><span>CAMPO</span><span>DORMIDO</span></h2>
      <div class="brand-dot" aria-hidden="true"></div>
      <div class="wine-details">
        <p class="vintage">Vintage 2024</p>
        <p class="region">DO Central Valley</p>
      </div>
    </footer>
  </main>
</body>
</html>
```